Stonefield Crafters Brochure = SCC $$$

this brochure will be used for a canvassing campaign (door to door) appointment setting

the campaign will be for homeowners that would like to do any kind of improvement to their house - home improvement
from EXT paint or roof repair all the way to kitchen and bathroom remodeling

we want to catch the prospect eye with the brochure and to educate our prospect about the different ways they could improve their house step by step to their dream house

Target Market(s)

Homeowners
anyone who would like to improve or fix any part of their house

Industry/Entity Type

Home Improvement

Contact Information for Business Card

the green roof house blueprints on one side
the Stonefield Crafters logo on the other side

Font styles to use
Serif
Decorative

Colors
ffffff
886aae
9bcb3b
e6e6e6

Requirements
Must have
• this is a TRI-FOLD brochure
• call for action -- schedule your free estimate
• or any idea that will lead to set up an appointment with our specialist
• LOOK AT MY WEBSITE TO UNDERSTAND MORE WHAT I LIKE
• WWW.STONEFIELDCRAFTERSCO.EXAMPLE
• services:
• Kitchen Renovations
• Bathroom Renovations
• Modern Landscaping
• Additions + in-law quarters
• Exterior paint +interior paint
• wood replacement + stucco repair
• roof repair
• railling and glass work
Nice to have
• the pictures I have uploaded can use as an example but im open to other ideas...
• THERE IS NO SUBSTITUTE FOR QUALITY.
• the picture of the women in the kitchen--
• i enjoy making food and spending time in my new kitchen, to see my whole family sitting down to eat dinner together in our perfect little kitchen make me so happy
Should not have
• the 2 brochures i have uploaded are for example only

```html
<!DOCTYPE html>
<html lang="en">
<head>
<meta charset="utf-8">
<title>Stonefield Crafters Tri-Fold Brochure</title>
<link rel="stylesheet" href="https://fonts.googleapis.com/css2?family=Playfair+Display:wght@700;800;900&family=Lato:wght@400;700;900&display=swap">
<style>
  :root {
    --green: #9bcb3b;
    --green-dark: #5f9a2a;
    --purple: #886aae;
    --charcoal: #3a3a3a;
    --ink: #262626;
    --paper: #ffffff;
    --mist: #e6e6e6;
    --stage: #ececec;
  }
  * { margin: 0; padding: 0; box-sizing: border-box; }
  html, body { width: 821px; height: 1200px; overflow: hidden; }
  body { background: var(--stage); font-family: "Lato", sans-serif; position: relative; }

  .sheet {
    position: absolute; left: 94px; width: 626px; height: 484px;
    background: var(--paper); overflow: hidden;
    box-shadow: 0 4px 14px rgba(0,0,0,.18);
  }
  .sheet--outside { top: 67px; }
  .sheet--inside { top: 636px; }
  .abs { position: absolute; }
  .art { position: absolute; left: 0; top: 0; }
  .serif { font-family: "Playfair Display", serif; }

  /* ---------- outside ---------- */
  .intro-title {
    left: 16px; top: 30px; color: var(--paper);
    font: 800 23px/26px "Playfair Display", serif;
  }
  .intro-text {
    left: 16px; top: 114px; width: 178px; color: var(--paper);
    font-size: 6.6px; line-height: 11.8px;
  }
  .about-title {
    left: 16px; top: 302px; color: var(--purple);
    font: 800 13px/16px "Playfair Display", serif;
  }
  .about-text {
    left: 16px; top: 346px; width: 178px; color: var(--ink);
    font-size: 6.6px; line-height: 11.8px;
  }
  .about-motto { left: 16px; top: 446px; font-size: 6.8px; font-weight: 700; color: var(--purple); }

  .hero-photo {
    left: 209px; top: 0; width: 417px; height: 484px;
    background: linear-gradient(100deg, #c99a2c 0%, #d8b14a 24%, #f1efec 34%, #e7e6e3 60%, #cfd0cc 100%);
  }
  .hero-fade {
    left: 209px; top: 320px; width: 417px; height: 164px;
    background: linear-gradient(to bottom, rgba(255,255,255,0) 0%, rgba(246,246,244,.94) 36%, #f4f4f2 100%);
  }
  .crest { left: 456px; top: 0; width: 138px; height: 84px; }
  .crest-dot { left: 516px; top: 10px; width: 18px; height: 18px; border-radius: 50%; background: var(--green-dark); }
  .crest-name {
    left: 456px; top: 33px; width: 138px; text-align: center;
    color: #6d6d6d; font: 700 8.5px/10px "Lato", sans-serif; letter-spacing: .8px;
  }

  .brand { display: flex; align-items: center; gap: 6px; }
  .brand-dot { width: 24px; height: 24px; border-radius: 50%; background: var(--green-dark); flex: none; }
  .brand-name { font: 700 10px/12px "Lato", sans-serif; color: var(--charcoal); letter-spacing: .6px; }
  .contact-brand { left: 224px; top: 356px; }
  .contact-phone { left: 224px; top: 398px; font: 700 17px/20px "Playfair Display", serif; color: var(--ink); }
  .contact-web { left: 224px; top: 426px; font-size: 6.5px; color: var(--ink); }
  .contact-address { left: 224px; top: 441px; font-size: 6.5px; line-height: 9px; color: var(--ink); }
  .promise {
    left: 433px; top: 388px; color: var(--ink);
    font: 800 20px/24px "Playfair Display", serif;
  }

  /* ---------- inside ---------- */
  .site-photo {
    left: 0; top: 0; width: 417px; height: 484px;
    background: linear-gradient(90deg, #8a5a32 0%, #c59a6a 22%, #e7e2d8 45%, #d8c3a0 70%, #9a6a3c 100%);
  }
  .kitchen-photo { left: 417px; top: 0; width: 209px; height: 484px;
    background: linear-gradient(180deg, #ececea 0%, #e2e2df 40%, #8a9097 55%, #d6a36d 78%, #b9824f 100%); }

  .callout-title {
    left: 433px; top: 14px; color: var(--green-dark);
    font: 700 13px/16px "Playfair Display", serif;
  }
  .callout-phone { left: 433px; top: 50px; font: 700 21px/24px "Playfair Display", serif; color: var(--ink); }
  .callout-text { left: 433px; top: 78px; width: 178px; font-size: 6.6px; line-height: 9px; color: var(--ink); }
  .estimate-button {
    left: 433px; top: 100px; width: 132px; height: 15px; border-radius: 8px;
    background: var(--purple); color: var(--paper); text-align: center;
    font: 900 6.6px/15px "Lato", sans-serif; letter-spacing: .5px;
  }
  .inside-brand { left: 512px; top: 447px; }
  .inside-brand .brand-name { color: var(--paper); }

  .badge-text {
    left: 114px; top: 297px; width: 80px; text-align: center;
    font: 900 7.2px/9.6px "Lato", sans-serif; color: var(--ink);
  }
  .motto-small { left: 16px; top: 349px; color: rgba(255,255,255,.85); font-size: 9.4px; line-height: 11px; }
  .motto-big { left: 16px; top: 396px; color: var(--paper); font: 900 23px/26px "Playfair Display", serif; }

  .services-title {
    left: 230px; top: 206px; width: 174px; text-align: right; color: var(--paper);
    font: 800 12px/14px "Playfair Display", serif;
  }
  .services { left: 229px; top: 242px; width: 176px; list-style: none; color: var(--paper); }
  .service { margin-bottom: 4.5px; }
  .service-name { font-size: 7px; font-weight: 900; line-height: 9px; }
  .service-text { font-size: 5.2px; line-height: 7px; opacity: .95; }
</style>
</head>
<body>

<section class="sheet sheet--outside">
  <svg class="art" width="626" height="484" viewBox="0 0 626 484" aria-hidden="true">
    <defs>
      <linearGradient id="fadeGray" x1="0" y1="0" x2="0" y2="1">
        <stop offset="0" stop-color="#d9d9d9"/><stop offset="1" stop-color="#ffffff"/>
      </linearGradient>
    </defs>
    <polygon points="0,232 209,330 209,360 0,300" fill="url(#fadeGray)"/>
    <polygon points="0,0 209,0 209,292 0,207" fill="var(--green)"/>
    <polygon points="0,207 209,292 209,312 0,220" fill="var(--purple)"/>
    <polygon points="0,220 209,312 209,330 0,232" fill="var(--charcoal)"/>
  </svg>

  <h1 class="abs intro-title">LET'S<br>CHANGE<br>YOUR LIVING.</h1>
  <p class="abs intro-text">Picture the perfect room. Everyone comes up with a different one: a cozy reading nook; a laser-filled bowling alley; a light-filled art studio. Ever wished you could bring your vision to reality? Tell us what you envision, and we'll help you bring it to life!</p>

  <h2 class="abs about-title">ABOUT<br>STONEFIELD CRAFTERS</h2>
  <p class="abs about-text">We believe that every project deserves the same kind of attention, no matter if it's a one room remodel or a new build of a multimillion dollar structure. To us, quality is achieving the best results, with the highest-grade material, at the lowest cost to you. That is how we define quality and that is what you're getting with Stonefield Crafters.</p>
  <p class="abs about-motto">We believe and live by our words...</p>

  <div class="abs hero-photo" role="img" aria-label="Bright modern home interior with a floating staircase, a mustard feature wall and a white dining area"></div>
  <div class="abs hero-fade"></div>

  <svg class="abs crest" width="138" height="84" viewBox="0 0 138 84" aria-hidden="true">
    <polygon points="0,0 138,0 138,56 69,84 0,56" fill="#f6f3e8"/>
  </svg>
  <span class="abs crest-dot"></span>
  <p class="abs crest-name">STONEFIELD<br>CRAFTERS</p>

  <div class="abs brand contact-brand"><span class="brand-dot"></span><span class="brand-name">STONEFIELD<br>CRAFTERS</span></div>
  <p class="abs contact-phone">(555) 014-2260</p>
  <p class="abs contact-web">www.stonefieldcraftersco.example</p>
  <p class="abs contact-address">418 Larkspur Ave. Suite 2,<br>Fairview, CA 90000</p>
  <p class="abs promise">THERE IS NO<br>SUBSTITUTE<br>FOR QUALITY.</p>
</section>

<section class="sheet sheet--inside">
  <div class="abs site-photo" role="img" aria-label="Homeowners reviewing building plans with a contractor in a framed room under renovation"></div>
  <div class="abs kitchen-photo" role="img" aria-label="Renovated family kitchen with grey cabinets, butcher-block island and wood floor"></div>

  <svg class="art" width="626" height="484" viewBox="0 0 626 484" aria-hidden="true">
    <polygon points="0,274 209,352 209,484 0,484" fill="var(--green)"/>
    <polygon points="209,250 417,150 417,484 209,484" fill="var(--green-dark)"/>
    <polygon points="417,0 626,0 626,100 417,193" fill="var(--paper)"/>
    <polygon points="417,193 626,100 626,110 417,207" fill="var(--green)"/>
    <polygon points="417,207 626,110 626,118 417,220" fill="var(--purple)"/>
    <polygon points="154,254 194,277 194,323 154,346 114,323 114,277" fill="var(--paper)"/>
    <circle cx="154" cy="274" r="9" fill="none" stroke="var(--purple)" stroke-width="1.6"/>
    <polyline points="149.5,274 153,277.5 159,270.5" fill="none" stroke="var(--purple)" stroke-width="1.8"/>
  </svg>

  <p class="abs callout-title">Living The Dream Is Just<br>One Phone Call Away.</p>
  <p class="abs callout-phone">(555) 014-2260</p>
  <p class="abs callout-text">Don't waste any more time, start your project with Stonefield Crafters, today!</p>
  <p class="abs estimate-button">SCHEDULE YOUR FREE ESTIMATE</p>

  <p class="abs badge-text">INNOVATIVE,<br>FULL SERVICE<br>DESIGN/BUILD</p>
  <p class="abs motto-small">Building a<br>better world<br>one day at a time.</p>
  <p class="abs motto-big">WE DESIGN<br>WE BUILD<br>WE CREATE</p>

  <h2 class="abs services-title">BUILD THE LIFE<br>OF YOUR DREAMS</h2>
  <ul class="abs services">
    <li class="service">
      <h3 class="service-name">Kitchen Renovations</h3>
      <p class="service-text">The Kitchen is the heart of the home. Make yours a place where the whole family sits down to dinner together.</p>
    </li>
    <li class="service">
      <h3 class="service-name">Bathroom Renovations</h3>
      <p class="service-text">Turn your Bathroom into a high-end spa right at home, a place of repose and rejuvenation after a long day.</p>
    </li>
    <li class="service">
      <h3 class="service-name">Modern Landscaping</h3>
      <p class="service-text">Be the neighbor with the amazing yard. We create beautiful, drought-tolerant gardens for a dry climate.</p>
    </li>
    <li class="service">
      <h3 class="service-name">Additions + In-Law Quarters</h3>
      <p class="service-text">Need more room? We design and build additions and in-law suites that blend right in with your home.</p>
    </li>
    <li class="service">
      <h3 class="service-name">Exterior + Interior Paint</h3>
      <p class="service-text">Fresh, lasting color inside and out, with careful prep and premium paints that protect your home.</p>
    </li>
    <li class="service">
      <h3 class="service-name">Wood Replacement + Stucco Repair</h3>
      <p class="service-text">We replace rotted wood and repair cracked stucco to keep your home sound, sealed and good looking.</p>
    </li>
    <li class="service">
      <h3 class="service-name">Roof Repair</h3>
      <p class="service-text">From a single leak to worn sections, we fix your roof fast so your family stays safe and dry.</p>
    </li>
    <li class="service">
      <h3 class="service-name">Railing + Glass Work</h3>
      <p class="service-text">Custom railings and glass panels for stairs, balconies and showers, built clean, strong and bright.</p>
    </li>
  </ul>

  <div class="abs brand inside-brand"><span class="brand-dot"></span><span class="brand-name">STONEFIELD<br>CRAFTERS</span></div>
</section>

</body>
</html>
```